Cleaning Company needs a new business card design

Hi, We are looking for new business card designs to update with our latest logo and company information.
We would like to see designs using the colours:
Royal Blue #4169E1 - this is our company colour so this has to be in there. Please feel free to experiment with other colours.
Must include:
Front of business card:
Logo
Back of the business card:
0800 529 6081
07438 915 702
Email: info@pkrtidyhomes.co.uk
Web: www.pkrtidyhomes.co.uk
Services:
End of Tenancy
Carpet & Upholstery
Regular & One Off
all work fully insured.
The front of the business card with the logo can be made to look raised print. The blue man to be a shiny finish.
The business card needs to be presented in a matt finish
The business must be in the following styles:
Standard Square with rounded corners.
Thank you to all that take part in this.
Target Market(s)
Men and Women of different ages in the UK.
Industry/Entity Type
House Cleaning
Contact Information for Business Card
Front of business card:
Logo
0800 529 6081
07438 915 702
Email: pkrtidy@mailbox-demo.co.uk
Services:
End of Tenancy
Carpet & Upholstery
Regular & One Off
all work fully insured.

```html
<!DOCTYPE html>
<html lang="en">
<head>
<meta charset="utf-8">
<title>PKR Tidy Homes – Business Card</title>
<link href="https://fonts.googleapis.com/css2?family=Arimo:wght@400;700&display=swap" rel="stylesheet">
<style>
  :root {
    --backdrop: #8f9092;
    --card-light: #e4e5e9;
    --card-navy: #283c8a;
    --brand-navy: #2b3d92;
    --brand-sky: #3a8fd0;
    --ink-grey: #3f4147;
    --ink-pale: #e6e8f0;
    --rule-light: #b9bbc2;
    --rule-navy: #5566a8;
  }
  * { margin: 0; padding: 0; box-sizing: border-box; }
  html, body {
    width: 1105px;
    height: 1200px;
    overflow: hidden;
    background: var(--backdrop);
    font-family: "Arimo", Arial, sans-serif;
  }
  .card {
    position: absolute;
    left: 182px;
    width: 746px;
    height: 425px;
    border-radius: 20px;
  }
  .card--front { top: 119px; background: var(--card-light); }
  .card--back  { top: 637px; background: var(--card-navy); }

  .brand {
    position: absolute;
    right: 400px;
    top: 188px;
    display: flex;
    align-items: center;
    gap: 12px;
  }
  .brand__dot {
    width: 26px;
    height: 26px;
    border-radius: 50%;
    background: var(--brand-sky);
  }
  .brand__name {
    font-size: 31px;
    font-weight: 700;
    white-space: nowrap;
    color: var(--brand-navy);
  }
  .card--back .brand__name { color: var(--ink-pale); }

  .divider {
    position: absolute;
    left: 372px;
    top: 136px;
    width: 1px;
    height: 155px;
  }
  .card--front .divider { background: var(--rule-light); }
  .card--back .divider { background: var(--rule-navy); }

  .details {
    position: absolute;
    left: 405px;
    top: 150px;
    list-style: none;
    font-size: 20.5px;
    line-height: 31px;
    letter-spacing: 0.2px;
  }
  .card--front .details { color: var(--ink-grey); }
  .card--back .details { color: var(--ink-pale); }
</style>
</head>
<body>
  <section class="card card--front">
    <div class="brand">
      <span class="brand__dot"></span>
      <span class="brand__name">PKR Tidy Homes</span>
    </div>
    <span class="divider"></span>
    <ul class="details">
      <li>0800 529 6081</li>
      <li>07438 915 702</li>
      <li>pkrtidy@mailbox-demo.co.uk</li>
      <li>pkrtidyhomes.co.uk</li>
    </ul>
  </section>

  <section class="card card--back">
    <div class="brand">
      <span class="brand__dot"></span>
      <span class="brand__name">PKR Tidy Homes</span>
    </div>
    <span class="divider"></span>
    <ul class="details">
      <li>End of Tenancy</li>
      <li>Carpet &amp; Upholstery</li>
      <li>Regular &amp; One Off</li>
      <li>ALL WORK FULLY INSURED.</li>
    </ul>
  </section>
</body>
</html>
```